Yoga class opening. Little schedule for JUNE JULY and AUGUST

Flyer to promote an opening yoga class. The color of the docx haven't to be respected.

We want something joyfull, professional, clean and serious.

About the logo we oppened a contest at the same time so at the moment there is no logo but the logo color will be simple.

The phone number will change so you can poste a random one for the design that i can change by myself.

i recieved many creation in both side BUT i want something in 1 side :)

Target Market(s)

Yoga student. all age

Industry/Entity Type

It Professional

Logo Text

Yoga fern

Font styles to use
Sans Serif

Requirements
Must have
• The text present on the docx
Nice to have
• Some symbols about yoga ( Namasté signs, mandala, ... )
Should not have
• Not too much details it has to be clear.

```html
<!DOCTYPE html>
<html lang="fr">
<head>
<meta charset="utf-8">
<title>Yoga fern – Stages d'été</title>
<link rel="stylesheet" href="https://fonts.googleapis.com/css2?family=Open+Sans:wdth,wght@75..100,300..800&display=swap">
<style>
  :root {
    --backdrop: #bdbdbd;
    --paper: #f6f7f8;
    --ink: #333333;
    --band: #323232;
    --sun: #f5b81c;
    --leaf: #6c9a2c;
    --field-top: #eef0ea;
    --field-mid: #a9bf6c;
    --field-low: #5f7f2a;
    --photo-light: #e6e4e6;
    --photo-tone: #d9c3c8;
  }
  * { box-sizing: border-box; margin: 0; padding: 0; }
  html, body { width: 1200px; height: 1200px; overflow: hidden; }
  body {
    background: var(--backdrop);
    font-family: "Open Sans", Arial, sans-serif;
    font-stretch: 78%;
    color: var(--ink);
  }
  .flyer {
    position: absolute; left: 220px; top: 62px;
    width: 760px; height: 1075px;
    background: var(--paper);
    overflow: hidden;
    box-shadow: 0 10px 30px rgba(0,0,0,.25);
  }
  .brand-corner {
    position: absolute; left: 0; top: 28px;
    width: 215px; height: 250px;
    background: var(--sun);
    border-bottom-right-radius: 100% 100%;
  }
  .brand-name {
    position: absolute; left: 38px; top: 80px;
    font-weight: 800; font-size: 44px; line-height: .95;
    text-transform: uppercase; color: var(--band);
    display: flex; flex-direction: column; align-items: flex-start; gap: 10px;
  }
  .brand-name .dot {
    width: 18px; height: 18px; border-radius: 50%; background: var(--band);
  }
  .header-band {
    position: absolute; left: 200px; top: 28px; right: 0; height: 112px;
    background: var(--band); color: #fff;
    display: flex; align-items: center; justify-content: center;
    text-align: center; font-weight: 700; font-size: 18px; line-height: 1.3;
    text-transform: uppercase; padding-left: 30px;
  }
  .intro {
    position: absolute; left: 230px; width: 510px; top: 152px;
    text-align: center; font-size: 13px; line-height: 1.4;
  }
  .photo { position: absolute; border-radius: 4px; }
  .photo-seated { left: 500px; top: 205px; width: 190px; height: 180px;
    background: radial-gradient(ellipse at 50% 45%, var(--photo-tone), var(--paper) 70%); }
  .photo-backbend { left: 160px; top: 455px; width: 170px; height: 210px;
    background: radial-gradient(ellipse at 50% 50%, var(--photo-light), var(--paper) 70%); }
  .photo-field { left: 0; right: 0; top: 560px; bottom: 0; border-radius: 0;
    background:
      radial-gradient(ellipse 30% 60% at 78% 40%, rgba(120,120,120,.35), transparent 70%),
      linear-gradient(to bottom, transparent 0, transparent 230px, var(--field-top) 300px, var(--field-mid) 400px, var(--field-low) 100%); }
  .month { position: absolute; font-size: 12.5px; line-height: 1.38; }
  .month h2 {
    display: flex; align-items: center; gap: 8px;
    color: var(--leaf); font-size: 20px; font-weight: 700; text-transform: uppercase;
    margin-bottom: 4px;
  }
  .month h2::before {
    content: ""; width: 16px; height: 16px; border-radius: 50%; background: var(--leaf);
  }
  .month p + p { margin-top: 10px; }
  .month-june { left: 40px; top: 275px; }
  .month-july { left: 360px; top: 405px; }
  .month-august { left: 150px; top: 680px; }
  .closing-band {
    position: absolute; left: 0; right: 0; top: 805px; height: 46px;
    background: var(--band); color: #fff;
    display: flex; align-items: center; padding-left: 50px; font-size: 14px;
  }
  .headline {
    position: absolute; left: 0; width: 560px; top: 868px; text-align: center;
    color: var(--leaf); font-weight: 700; font-size: 40px; text-transform: uppercase;
  }
  .contact {
    position: absolute; left: 50px; top: 968px; color: #fff; font-size: 15px; line-height: 1.45;
  }
  .contact-line { display: flex; align-items: center; gap: 7px; }
  .contact-line svg { width: 13px; height: 13px; }
  .social-square { width: 12px; height: 12px; background: #fff; }
</style>
</head>
<body>
<article class="flyer">
  <div class="photo photo-field" role="img" aria-label="Photo d'une femme en posture du guerrier sur un tapis dans une prairie verte au soleil"></div>

  <div class="brand-corner">
    <div class="brand-name"><span class="dot"></span><span>Yoga<br>fern</span></div>
  </div>

  <header class="header-band">
    Nouveau !! Votre studio de yoga à Ixelles<br>
    ouverture le 6 juin 2016 au<br>
    12 Rue des Tilleuls, 1050 Ixelles
  </header>

  <p class="intro">En attendant le planning des cours de la rentrée, YOGA FERN vous propose<br>ses stages et ateliers d'été.</p>

  <div class="photo photo-seated" role="img" aria-label="Photo d'une femme assise en posture du lotus, en méditation"></div>
  <div class="photo photo-backbend" role="img" aria-label="Photo d'une femme en posture de flexion arrière"></div>

  <section class="month month-june">
    <h2>Juin</h2>
    <p>Stage découverte du YOGA 10h00 85 € :<br>
    Du lundi 6 au vendredi 10 juin : 10h00 à 12h00 ou 18h00 à 20h00<br>
    Du lundi 13 au vendredi 17 juin : 10h00 à 12h00 ou 18h00 à 20h00<br>
    Du lundi 20 au vendredi 24 juin : 10h00 à 12h00 ou 18h00 à 20h00<br>
    Du lundi 27 au vendredi 1er juillet : 10h00 à 12h00 ou 18h00 à 20h00</p>
    <p>Atelier gestion du stress yoga/sophrologie 2h00 28 €<br>
    Samedi 11 juin 10h30 à 12h30<br>
    Samedi 11 juin 15h à 17h00<br>
    Dimanche 12 juin 10h30 à 12h30<br>
    Dimanche 12 juin 14h à 16h00</p>
  </section>

  <section class="month month-july">
    <h2>Juillet</h2>
    <p>Stage initiation à l'ASHTANGA 10h00 85 €<br>
    Du lundi 4 au vendredi 8 juillet : 10h00 à 12h00 ou 18h00 à 20h00<br>
    Du lundi 11 au vendredi 15 juillet : 10h00 à 12h00 ou 18h00 à 20h00<br>
    Du lundi 18 au vendredi 22 juillet : 10h00 à 12h00 ou 18h00 à 20h00<br>
    Du lundi 25 au vendredi 29 juillet : 10h00 à 12h00 ou 18h00 à 20h00</p>
    <p>Atelier gestion du stress yoga/sophrologie 2h00 28 €<br>
    Samedi 9 juillet 10h30 à 12h30<br>
    Samedi 9 juillet 15h00 à 17h00<br>
    Dimanche 10 juillet 10h30 à 12h30<br>
    Dimanche 10 juillet 14h00 à 16h00</p>
  </section>

  <section class="month month-august">
    <h2>Août</h2>
    <p>Stage découverte du YOGA 10h00 85 €<br>
    Du lundi 1er au vendredi 5 août : 10h00 à 12h00 ou 18h00 à 20h00<br>
    Du lundi 8 au vendredi 12 août : 10h00 à 12h00 ou 18h00 à 20h00<br>
    Du lundi 15 au vendredi 19 août : 10h00 à 12h00 ou 18h00 à 20h00<br>
    Du lundi 22 au vendredi 26 août : 10h00 à 12h00 ou 18h00 à 20h00</p>
  </section>

  <div class="closing-band">Démarrage du planning annuel le 5 septembre 2016</div>
  <p class="headline">Un bel été à tous !</p>

  <footer class="contact">
    <p>Plus d'info et inscription :</p>
    <p class="contact-line">
      <svg viewBox="0 0 24 24" aria-hidden="true"><path fill="#fff" d="M6.6 10.8a15 15 0 0 0 6.6 6.6l2.2-2.2a1 1 0 0 1 1-.25 11.4 11.4 0 0 0 3.6.57 1 1 0 0 1 1 1V20a1 1 0 0 1-1 1A17 17 0 0 1 3 4a1 1 0 0 1 1-1h3.5a1 1 0 0 1 1 1c0 1.25.2 2.45.57 3.57a1 1 0 0 1-.25 1z"/></svg>
      +32-470-10-20-30
    </p>
    <p class="contact-line"><span class="social-square"></span>yogafern</p>
  </footer>
</article>
</body>
</html>
```